Webbanner-Design für Prairiefolk Shop
Zielgruppe
Online Shop Westernartikel
Aufgabenstellung
Wir verkaufen über unseren Online Shop ( www.prairiefolk-ranchhaus-shop.de ) Westernbekleidung und Westernreitzubehör ( Buckaroo / Vaquero orientiert ).
Wir beziehen einen großen Teil der Ware aus den Staaten. Ich benötige einen Banner der den Alten ersetzt. Ein neues Logo wurde gestaltet, ist aber noch nicht freigegeben.
Wird das Logo benötigt so kann ich dieses unter Vorbehalt zur Verfügung stellen.
Könnte für das Logo ein Platzhalter vorgesehen werden?
Derzeitige Bannergröße ist 978 x 269

```html
<!DOCTYPE html>
<html lang="en">
<head>
<meta charset="utf-8">
<title>Prairiefolk Shop – start page</title>
<link href="https://fonts.googleapis.com/css2?family=Arimo:wght@400;700&display=swap" rel="stylesheet">
<style>
:root{
  --backdrop:#5c5454;
  --page:#ffffff;
  --dark:#3b3838;
  --dark-2:#2a2828;
  --orange:#f07e00;
  --orange-deep:#d66300;
  --link:#8a3a10;
  --text:#222222;
  --muted:#555555;
  --footer:#eeeeee;
}
*{box-sizing:border-box;margin:0;padding:0}
html,body{width:903px;height:1200px;overflow:hidden;background:var(--backdrop)}
body{font-family:"Arimo",Arial,sans-serif;color:var(--text);letter-spacing:.3px}
.stage{position:absolute;left:0;top:0;width:1366px;height:1815px;transform:scale(.6611);transform-origin:0 0}
.abs{position:absolute}

.utility-bar{left:622px;top:10px;width:561px;height:25px;background:var(--dark);display:flex;align-items:center;font-size:12px;color:#fff;letter-spacing:0}
.utility-bar span{padding:0 9px;border-left:1px solid #5a5656;line-height:25px;white-space:nowrap}
.utility-bar span:first-child{border-left:0;padding:0 10px}
.caret{display:inline-block;border:4px solid transparent;border-top-color:#fff;border-bottom:0;margin-left:6px;vertical-align:2px}

.page{left:183px;top:35px;width:1000px;height:1770px;background:var(--page)}

.banner{left:193px;top:47px;width:979px;height:269px;background:linear-gradient(100deg,#7b6651 0%,#a08770 35%,#8e7760 60%,#6e5b48 100%);overflow:hidden}
.wordmark{position:absolute;left:34px;top:99px;width:204px;height:72px;background:#fff;border-radius:12px;display:flex;align-items:center;justify-content:center;text-align:center;font-weight:700;font-size:21px;letter-spacing:2px;line-height:1.05;color:#1b1b1b}
.circle{position:absolute;border-radius:50%;border:5px solid rgba(255,255,255,.55)}
.circle.hat{left:474px;top:40px;width:190px;height:190px;background:radial-gradient(circle,#ffffff 40%,#e4e4e4)}
.circle.rider{left:640px;top:40px;width:180px;height:190px;background:linear-gradient(160deg,#e7ebef,#b8a070 60%,#4a3d30)}
.circle.boot{left:772px;top:40px;width:190px;height:190px;background:radial-gradient(circle,#b86a38,#e9c6a0 75%)}

.nav{left:193px;width:979px;height:29px;background:linear-gradient(#f58a12,var(--orange-deep));display:flex;align-items:center;padding-left:8px;font-size:15px;color:#fff;letter-spacing:0}
.nav span{padding:0 9px;border-left:1px solid rgba(255,255,255,.45);line-height:17px}
.nav span:first-child{border-left:0}

.toolbar{left:193px;top:378px;width:979px;height:38px;background:var(--dark);letter-spacing:0}
.search-field{position:absolute;left:8px;top:8px;width:135px;height:22px;background:#fff;border:1px solid #999;font-size:12px;color:#666;padding:3px 3px}
.search-go{position:absolute;left:148px;top:8px;width:35px;height:22px;background:#1f1d1d;border:1px solid #555;color:#fff;font-size:11px;font-weight:700;text-align:center;line-height:20px}
.crumb{position:absolute;left:220px;top:13px;color:#fff;font-size:15px}
.cart-divider{position:absolute;left:775px;top:8px;width:1px;height:22px;background:#666}
.cart-icon{position:absolute;left:800px;top:9px}
.cart-label{position:absolute;left:880px;top:6px;color:#fff;font-size:12px;font-weight:700;text-align:center;line-height:14px}
.cart-label small{display:block;font-size:9px}

.box{left:193px;width:202px;border:1px solid #d3d3d3;background:#fff}
.box-head{height:25px;background:linear-gradient(#4a4646,var(--dark-2));color:#fff;font-size:13px;font-weight:700;line-height:25px;padding-left:10px;position:relative}
.box-body{padding:6px 10px;font-size:12px;color:var(--muted)}
.field{display:block;width:180px;height:22px;border:1px solid #888;margin:4px 0 8px}
.login-btn{display:block;margin:0 0 0 auto;width:52px;height:22px;background:#1f1d1d;color:#fff;font-size:11px;text-align:center;line-height:22px}
.seller{border-bottom:1px dotted #aaa;padding:6px 0 3px;font-size:12px;line-height:14px}
.seller b{color:#444}
.seller a{color:var(--link);text-decoration:none}
.seller .price{text-align:right;color:var(--muted)}
.news p{color:var(--link);font-style:italic;font-weight:700;font-size:14px;text-align:center;margin-bottom:14px;line-height:16px}
.news .u{text-decoration:underline dashed}
.list{list-style:none;font-size:12px;color:var(--text);line-height:14px}
.list li::before{content:"";display:inline-block;border:3px solid transparent;border-left-color:#333;border-right:0;margin-right:4px}
.play{position:absolute;right:10px;top:6px;width:13px;height:13px;border-radius:50%;background:#999}
.ph{display:block}

.main{left:413px;width:760px}
.welcome-title{top:428px;font-size:12px;font-weight:700}
.welcome-line{top:453px;font-size:12px}
.intro{top:506px;font-size:13.4px;font-weight:700;line-height:16px;letter-spacing:.55px}
.intro .url{color:var(--orange)}
.section-title{font-size:20px;color:#444;font-weight:400;letter-spacing:0}
.grid{display:grid;grid-template-columns:repeat(4,190px)}
.card{height:284px;border-left:1px dotted #bbb;position:relative}
.card:first-child,.card:nth-child(5){border-left:0}
.card .ph{position:absolute;top:16px;left:50%;transform:translateX(-50%)}
.card .name{position:absolute;left:15px;right:15px;top:167px;font-size:12px;font-weight:700;color:#333;line-height:14px}
.card .price{position:absolute;right:18px;top:234px;font-size:14px;font-weight:700}
.card::after{content:"";position:absolute;left:15px;right:15px;bottom:18px;border-bottom:1px dotted #aaa}
.card:last-child{border-right:1px dotted #bbb}

.footer{left:183px;top:1767px;width:1000px;height:38px;background:var(--footer);text-align:center}
.footer b{display:block;color:var(--link);font-size:14px;margin-top:2px}
.footer small{display:block;color:#444;font-size:11px;font-weight:700;margin-top:3px}
</style>
</head>
<body>
<div class="stage">
  <div class="abs utility-bar">
    <span><svg width="13" height="12" viewBox="0 0 13 12"><path d="M6.5 0 0 6h2v6h3.5V8h2v4H11V6h2z" fill="#fff"/></svg></span>
    <span>Location: Germany<i class="caret"></i></span>
    <span>Welcome back<i class="caret"></i></span>
    <span>Customer group: Guest</span>
    <span>Leaflet</span>
    <span>Shopping</span>
  </div>

  <div class="abs page"></div>

  <header class="abs banner" role="img" aria-label="Western rider on a horse in a sandy arena, with round photos of a black hat, a rider in a yellow slicker and a brown cowboy boot">
    <div class="circle rider"></div>
    <div class="circle hat"></div>
    <div class="circle boot"></div>
    <div class="wordmark">PRAIRIEFOLK<br>RANCHHAUS</div>
  </header>

  <nav class="abs nav" style="top:318px"><span>Ranch Wear</span><span>Ranch Horse</span><span>Specials</span></nav>
  <nav class="abs nav" style="top:348px"><span>Search</span><span>Ranchland</span><span>about us</span></nav>

  <div class="abs toolbar">
    <div class="search-field">Suche...</div>
    <div class="search-go">Go</div>
    <div class="crumb">start page</div>
    <div class="cart-divider"></div>
    <svg class="cart-icon" width="26" height="20" viewBox="0 0 26 20"><path d="M1 6h24l-3 13H4z" fill="#666"/><path d="M7 6l4-5M19 6l-4-5" stroke="#666" stroke-width="2"/></svg>
    <div class="cart-label">Your Cart <i class="caret" style="border-top-color:#999;margin-left:14px"></i><small>no products</small></div>
  </div>

  <aside class="abs box" style="top:428px;height:196px">
    <div class="box-head">Welcome back!</div>
    <div class="box-body">
      E-mail address<span class="field"></span>
      password<span class="field"></span>
      <span class="login-btn">Log In</span>
      <div style="margin-top:17px;line-height:14px">Create account<br>Forgot your password?</div>
    </div>
  </aside>

  <aside class="abs box" style="top:635px;height:278px">
    <div class="box-head">bestseller</div>
    <div class="box-body" style="padding-top:0">
      <div class="seller"><b>01.</b> <a>Pommel Rider Slicker</a><div class="price">78.00 EUR</div></div>
      <div class="seller"><b>02.</b> <a>Men`s Bronco Canvas<br>Vest</a><div class="price">39.00 EUR</div></div>
      <div class="seller"><b>03.</b> <a>Silk Solid Wild Rag 34.5 "</a><div class="price">18.00 EUR</div></div>
      <div class="seller"><b>04.</b> <a>Jacquard Silk Wild Rag</a><div class="price">34.00 EUR</div></div>
      <div class="seller"><b>05.</b> <a>Men`s Wyoming Wool<br>Vest</a><div class="price">59.00 EUR</div></div>
    </div>
  </aside>

  <aside class="abs box" style="top:925px;height:172px">
    <div class="box-head">deals<span class="play"></span></div>
    <div class="box-body" style="text-align:center">
      <div class="ph" role="img" aria-label="Red and black saddle blanket" style="width:100px;height:75px;margin:2px auto 20px;background:linear-gradient(#b8353c,#3e3a3a 50%,#b8353c)"></div>
      Saddle Blanket<div style="margin-top:14px">only 50,00 EUR</div>
    </div>
  </aside>

  <aside class="abs box" style="top:1108px;height:107px">
    <div class="box-head">Counter</div>
    <div class="box-body" style="line-height:14px">2 visitors<br>currently online<br><br>20396 Visitors<br>since 01.01.2016</div>
  </aside>

  <aside class="abs box news" style="top:1226px;height:249px">
    <div class="box-head">News</div>
    <div class="box-body" style="padding-top:62px">
      <p>Ashford Vaquero style hats from the States</p>
      <p><span class="u">Crooked Y Boots for</span><br>special prices</p>
      <p>Trailhand Jeans for<br>55.- €</p>
    </div>
  </aside>

  <aside class="abs box" style="top:1486px;height:49px">
    <div class="box-head">informations</div>
    <ul class="box-body list" style="padding-top:5px"><li>Sitemap</li></ul>
  </aside>

  <aside class="abs box" style="top:1547px;height:148px">
    <div class="box-head">More about...</div>
    <ul class="box-body list" style="padding-top:6px">
      <li>Imprint</li><li>Conditions</li><li>Privacy</li><li>Withdrawal &amp; model<br>withdrawal form</li><li>Shipping &amp; Returns</li><li>Shipping &amp; payment</li><li>Contact</li>
    </ul>
  </aside>

  <div class="abs main welcome-title">welcome</div>
  <div class="abs main welcome-line">Welcome Guest! Would you like to login ? Or you want a customer account open?</div>
  <p class="abs main intro">We offer in our <span class="url">www.prairiefolk-ranchhaus-shop.de</span> (Prairiefolk Shop) enhanced products like Western clothing, Western Hats, Cowboy Boots, Western Horse equipment and other Western products, most are drawn from the states. We also carry selected Vaquero / Buckaroo products. Products as saddles, end caps, belts and Chaps / Chinks are Custom Made / Handmade and are also referred to as such in the description. If you are interested in a saddle or chaps / Chinks this can be discussed only in person (see contact). Western horse accessories such as headpieces, spurs, bits, leashes and many more we have available, if they are not listed in Prairiefolk Internet shop, we would (see contact) welcome inquiries. The reproduction of images and colors may vary from the original.</p>

  <h2 class="abs main section-title" style="top:789px">deals</h2>
  <div class="abs main grid" style="top:826px">
    <div class="card"><div class="ph" role="img" aria-label="Stack of coloured wool saddle pads" style="width:95px;height:100px;background:linear-gradient(135deg,#6b3552,#2c5a4a 50%,#1e3a6a)"></div><div class="name">PF32-Super Roper, Rhombus Wool Pad</div><div class="price">Only 95.00 EUR</div></div>
    <div class="card"><div class="ph" role="img" aria-label="Black and tan women's horseman boot" style="width:75px;height:100px;background:linear-gradient(#b59e86,#2a2627 60%,#7a6a5c)"></div><div class="name">Womens Horseman (only size 8)</div><div class="price">Only 179,00 EUR</div></div>
    <div class="card"><div class="ph" role="img" aria-label="Red and black saddle blanket" style="width:100px;height:75px;background:linear-gradient(#b8353c,#3e3a3a 50%,#b8353c)"></div><div class="name">Saddle Blanket</div><div class="price">Only 50,00 EUR</div></div>
    <div class="card"><div class="ph" role="img" aria-label="Brown and black men's cattleman boot" style="width:75px;height:100px;background:linear-gradient(#c2ac95,#2a2627 45%,#9a5a34)"></div><div class="name">Mens Cattleman (only size 11)</div><div class="price">Only 179,00 EUR</div></div>
    <div class="card"><div class="ph" role="img" aria-label="Dark green wool bomber jacket" style="width:100px;height:75px;background:linear-gradient(#f2f2f2,#2d3a25 30%,#1f2a1a)"></div><div class="name">Wool Bomber Jacket in Black / XL</div><div class="price">Only 79,00 EUR</div></div>
    <div class="card"><div class="ph" role="img" aria-label="Brown and black women's cattleman boot" style="width:75px;height:100px;background:linear-gradient(#c2ac95,#2a2627 45%,#9a5a34)"></div><div class="name">Womens Cattleman (only size 8)</div><div class="price">Only 179,00 EUR</div></div>
    <div class="card"><div class="ph" role="img" aria-label="Black felt saddle pad" style="width:100px;height:60px;background:linear-gradient(#fff 10%,#222 20%,#111 80%,#fff 90%)"></div><div class="name">PF21L-Wool Felt Pad, Rhombus Wool Pad</div><div class="price">Only 79,00 EUR</div></div>
    <div class="card"><div class="ph" role="img" aria-label="Black felt saddle pad" style="width:80px;height:60px;background:linear-gradient(#fff 10%,#222 20%,#111 70%,#fff 80%)"></div><div class="name">PF71L-Wool Felt Pad, Rhombus Wool Pad</div><div class="price">Only 79,00 EUR</div></div>
  </div>

  <h2 class="abs main section-title" style="top:1421px">New products</h2>
  <div class="abs main grid" style="top:1458px">
    <div class="card" style="border-right:1px dotted #bbb"><div class="ph" role="img" aria-label="Coiled blue and purple kids rope" style="width:100px;height:56px;background:radial-gradient(circle,#b9a395 20%,#4a6b9a 35%,#6a4a8a 50%,#b9a395 60%)"></div><div class="name">Kids Rope (Loop Master)</div><div class="price">21.00 EUR</div></div>
  </div>

  <footer class="abs footer">
    <b>The Prairiefolk Shop Team thanks for visiting.</b>
    <small>Shop Software by Shopwerk.de © 2010</small>
  </footer>
</div>
</body>
</html>
```